A r&b and house DJ needs a new Graphically pleasing and trendy website for fans and potential client

Want a new design for a dj website. This website wont be updated often so needs to look very graphically pleasing and just be a point of call where fans and potential clients can come and see information about the dj etc.

Needs to have short bio , social network links, and a enquiry button.

You can use some stock images for the moment as some professional images are going to be taken.

Others DJ websites:

https://www.djvorrelan.com/
http://www.pelicorvane.com/
http://quibon.com/
http://umerko.com/
http://www.dorianpuckett.co.uk/gb/home
http://www.florvimmel.com/
http://pranelo.nl/

LOGO LINK IS HERE

https://www.filecrate.example/s/k7wmq3zr9xn2vle/DJ_Wembo_logo.eps?dl=0

Target Market(s)

Fans and also prospective clients ( Nightclubs, Record Labels)

Industry/Entity Type

House

Font styles to use
Sans Serif

Requirements
Must have
• Small Bio, Social Network Links, Enquiry Button.
Nice to have
• Social network links

```html
<!DOCTYPE html>
<html lang="en">
<head>
<meta charset="utf-8">
<title>Velvet Groove R &amp; B</title>
<link rel="stylesheet" href="https://fonts.googleapis.com/css2?family=Oswald:wght@400&family=Roboto:wght@400;500&family=Open+Sans:wght@400;600&display=swap">
<style>
:root{
  --page:#2c2c2e;
  --panel:#353537;
  --panel-dark:#1b1b1c;
  --black:#050505;
  --red:#d0100f;
  --red-dark:#a30b0a;
  --white:#ffffff;
  --muted:#9a9a9c;
  --line:#2a2a2c;
  --gold:#e2a013;
}
*{box-sizing:border-box;margin:0;padding:0}
html,body{width:814px;height:1200px;overflow:hidden}
body{background:var(--page);font-family:"Roboto",Arial,sans-serif;color:var(--white);position:relative}
.abs{position:absolute}

/* hero */
.hero{left:0;top:0;width:814px;height:468px;background:radial-gradient(ellipse at 55% 35%,#8a7e72 0%,#4a423c 30%,#1c1a1c 65%,#0b0b0e 100%)}
.hero-glow{left:80px;top:120px;width:200px;height:160px;background:radial-gradient(ellipse,rgba(70,170,255,.55),rgba(70,170,255,0) 70%)}
.site-header{left:0;top:0;width:814px;height:70px;background:rgba(30,30,30,.82);border-bottom:1px solid #3a3a3a}
.brand{left:66px;top:22px;display:flex;align-items:center;gap:8px;font-family:"Oswald",sans-serif;font-size:22px;color:var(--white);letter-spacing:-.3px}
.brand-mark{width:22px;height:22px;border-radius:50%;background:var(--white)}
.enquiry{left:674px;top:26px;width:73px;height:25px;border:1px solid #d8d8d8;border-radius:2px;font-size:11.5px;display:flex;align-items:center;justify-content:center;letter-spacing:.3px}
.arrow{top:256px;width:36px;height:36px}
.welcome{left:66px;top:360px;width:681px;height:108px;background:rgba(0,0,0,.45);border:1px solid #8a8a8a;border-bottom:none;padding:16px 26px}
.welcome h1{font-family:"Oswald",sans-serif;font-weight:400;font-size:19px;letter-spacing:-.2px;margin-bottom:12px}
.welcome h1 span{color:var(--red)}
.welcome p{font-size:11.4px;line-height:18px;color:#eee}

/* nav */
.main-nav{left:0;top:468px;width:814px;height:42px;background:linear-gradient(#d7120f,#b00d0b)}
.main-nav a{position:absolute;top:0;height:42px;display:flex;align-items:center;justify-content:center;font-size:11.5px;color:var(--white);text-decoration:none;border-right:1px solid rgba(0,0,0,.2)}
.main-nav a.active{background:#2b2b2b}

/* sections */
.section-title{font-size:12.5px;letter-spacing:.3px;top:525px}
.panel{background:var(--panel)}
.photo{display:block}
.video-caption{font-family:"Open Sans",sans-serif;font-size:7.5px;line-height:14px;color:var(--muted);padding:10px 13px}
.play{fill:none;stroke:rgba(255,255,255,.45);stroke-width:2}
.player{left:299px;top:551px;width:213px;height:35px;border:3px solid var(--red);background:#2a2a2a}
.track{height:28px;border-top:1px solid var(--line);display:flex;align-items:center;font-family:"Open Sans",sans-serif;font-size:8.6px;color:var(--muted)}
.track i{width:27px;height:100%;border-right:1px solid var(--line);display:flex;align-items:center;justify-content:center}
.track span{padding-left:12px}
.event{height:52px;border-bottom:1px solid var(--line);display:flex;align-items:center;padding-left:8px}
.event-icon{width:29px;height:29px;background:var(--red);display:flex;align-items:center;justify-content:center;margin-right:14px;flex:none}
.event h3{font-family:"Roboto",sans-serif;font-weight:400;font-size:9px;color:var(--muted);letter-spacing:.2px}
.event p{font-family:"Open Sans",sans-serif;font-size:7.5px;color:#8a8a8c;margin-top:5px}

.popular-bar{left:67px;top:790px;width:445px;height:40px;background:var(--black);border:1px solid #3d3d3d;display:flex;align-items:center;justify-content:space-between;padding:0 13px}
.popular-bar h2{font-weight:400;font-size:13.5px;letter-spacing:.3px}
.card{top:850px;width:213px;height:254px;background:var(--black)}
.card p{font-family:"Open Sans",sans-serif;font-size:9.4px;line-height:15px;color:#a9a9ab;padding:9px 10px;height:56px}
.card .meta{border-top:1px solid #2a2a2a;font-family:"Open Sans",sans-serif;font-size:7.4px;color:#ccc;padding:7px 10px}
.card .meta b{color:var(--gold);text-decoration:underline;font-weight:600}

.albums{left:534px;top:790px;width:213px;height:316px;background:var(--black);border:1px solid #3d3d3d}
.albums h2{font-weight:500;font-size:11px;height:40px;display:flex;align-items:center;padding-left:16px;border-bottom:1px solid #2a2a2a}
.album{height:92px;border-bottom:1px solid #2a2a2a;display:flex;padding:13px 0 0 17px}
.album:last-child{border-bottom:none}
.album .thumb{width:66px;height:54px;margin-right:12px;flex:none}
.album h3{font-weight:400;font-size:9.4px;color:var(--muted);margin-top:0}
.album p{font-family:"Open Sans",sans-serif;font-size:7.3px;line-height:13.5px;color:#8e8e90;margin-top:4px}
.stars{margin-top:3px;display:flex;gap:1px}

.site-footer{left:0;top:1124px;width:814px;height:76px;background:var(--black)}
.social{left:314px;top:19px;display:flex;gap:5px}
.social span{width:21px;height:21px;border-radius:50%;background:#5a5a5c}
.copyright{left:0;top:48px;width:814px;text-align:center;font-size:8px;color:#8a8a8c}
</style>
</head>
<body>

<div class="abs hero" role="img" aria-label="Photo of a hooded DJ in sunglasses and headphones reaching out with glowing blue light at a mixing deck"></div>
<div class="abs hero-glow"></div>

<header class="abs site-header">
  <div class="abs brand"><span class="brand-mark"></span>VELVET GROOVE R &amp; B</div>
  <a class="abs enquiry">ENQUIRY</a>
</header>

<svg class="abs arrow" style="left:32px" viewBox="0 0 36 36"><path d="M18 2 34 18 18 34 2 18Z" fill="rgba(0,0,0,.2)" stroke="#fff" stroke-width="1.3"/><path d="M20 13 15 18 20 23" fill="none" stroke="#fff" stroke-width="2"/></svg>
<svg class="abs arrow" style="left:740px" viewBox="0 0 36 36"><path d="M18 2 34 18 18 34 2 18Z" fill="rgba(0,0,0,.2)" stroke="#fff" stroke-width="1.3"/><path d="M16 13 21 18 16 23" fill="none" stroke="#fff" stroke-width="2"/></svg>

<section class="abs welcome">
  <h1>WELCOME TO <span>VELVET GROOVE R &amp; B</span></h1>
  <p>Lorem Ipsum has been the industry’s standard dummy text ever since the 1500s, when an unknown printer took a galley<br>of type and scrambled it to make a type specimen book. It has survived not only five centuries</p>
</section>

<nav class="abs main-nav">
  <a class="active" style="left:66px;width:58px">NEWS</a>
  <a style="left:124px;width:68px">TOUR</a>
  <a style="left:192px;width:68px">MUSIC</a>
  <a style="left:260px;width:66px">MEDIA</a>
  <a style="left:326px;width:70px">SOCIAL</a>
  <a style="left:396px;width:69px">RADIO</a>
  <a style="left:465px;width:104px">FOUNDATION</a>
  <a style="left:569px;width:69px">STORE</a>
  <a style="left:638px;width:109px;border-right:none">GET UPDATES</a>
</nav>

<h2 class="abs section-title" style="left:67px;font-weight:400">VIDEO</h2>
<h2 class="abs section-title" style="left:299px;font-weight:400">MUSIC</h2>
<h2 class="abs section-title" style="left:533px;font-weight:400">FEATURED EVENTS</h2>

<article class="abs panel" style="left:67px;top:551px;width:212px;height:207px">
  <div class="photo" style="height:158px;background:linear-gradient(135deg,#d9b37a,#6b4a2c 45%,#1f1814)" role="img" aria-label="Video still of a woman in headphones dancing against a city skyline at night"></div>
  <svg class="abs" style="left:80px;top:52px" width="52" height="52" viewBox="0 0 52 52"><circle class="play" cx="26" cy="26" r="24"/><path d="M21 16 36 26 21 36Z" fill="rgba(255,255,255,.45)"/></svg>
  <p class="video-caption">Sed ut perspiciatis unde omnis iste natus error sit<br>voluptatem accusantium doloremque</p>
</article>

<div class="abs player">
  <svg width="207" height="29" viewBox="0 0 207 29">
    <g fill="none" stroke="#777" stroke-width="1"><circle cx="14" cy="14.5" r="6"/><circle cx="34" cy="14.5" r="6"/><circle cx="54" cy="14.5" r="6"/></g>
    <path d="M12 12v5M16 12v5" stroke="#777"/><path d="M32 11.5 37 14.5 32 17.5Z" fill="#777"/><path d="M52 12v5M56 12v5" stroke="#777"/>
    <rect x="74" y="13.5" width="112" height="2.5" fill="#777"/>
    <path d="M193 12.5h2l3-2.5v9l-3-2.5h-2Z" fill="#777"/>
  </svg>
</div>
<div class="abs panel" style="left:299px;top:586px;width:213px;height:172px">
  <div class="track" style="border-top:none"><i><svg width="7" height="6"><path d="M1 5V3.5a2.5 2.5 0 0 1 5 0V5" fill="none" stroke="#666"/></svg></i><span>Sed ut perspiciatis unde omnis</span></div>
  <div class="track"><i><svg width="7" height="6"><path d="M1 5V3.5a2.5 2.5 0 0 1 5 0V5" fill="none" stroke="#666"/></svg></i><span>Nemo enim ipsam voluptatem quia</span></div>
  <div class="track"><i><svg width="7" height="6"><path d="M1 5V3.5a2.5 2.5 0 0 1 5 0V5" fill="none" stroke="#666"/></svg></i><span>vel illum qui dolorem eum fugiat</span></div>
  <div class="track"><i><svg width="7" height="6"><path d="M1 5V3.5a2.5 2.5 0 0 1 5 0V5" fill="none" stroke="#666"/></svg></i><span>Quis autem vel eum iure reprehenderit</span></div>
  <div class="track"><i><svg width="7" height="6"><path d="M1 5V3.5a2.5 2.5 0 0 1 5 0V5" fill="none" stroke="#666"/></svg></i><span>Lorem ipsum dolor sit amet</span></div>
  <div class="track"><i><svg width="7" height="6"><path d="M1 5V3.5a2.5 2.5 0 0 1 5 0V5" fill="none" stroke="#666"/></svg></i><span>Ut enim ad minim veniam</span></div>
</div>

<div class="abs panel" style="left:534px;top:551px;width:212px;height:207px">
  <div class="event"><div class="event-icon"><svg width="14" height="12"><path d="M2 10V7a5 5 0 0 1 10 0v3" fill="none" stroke="#fff" stroke-width="2"/><rect x="1" y="7" width="3" height="4" fill="#fff"/><rect x="10" y="7" width="3" height="4" fill="#fff"/></svg></div><div><h3>SED UT PERSPICIATIS UNDE OMNIS</h3><p>Nemo enim ipsam voluptatem quia</p></div></div>
  <div class="event"><div class="event-icon"><svg width="14" height="12"><path d="M2 10V7a5 5 0 0 1 10 0v3" fill="none" stroke="#fff" stroke-width="2"/><rect x="1" y="7" width="3" height="4" fill="#fff"/><rect x="10" y="7" width="3" height="4" fill="#fff"/></svg></div><div><h3>SED UT PERSPICIATIS UNDE OMNIS</h3><p>Nemo enim ipsam voluptatem quia</p></div></div>
  <div class="event"><div class="event-icon"><svg width="14" height="12"><path d="M2 10V7a5 5 0 0 1 10 0v3" fill="none" stroke="#fff" stroke-width="2"/><rect x="1" y="7" width="3" height="4" fill="#fff"/><rect x="10" y="7" width="3" height="4" fill="#fff"/></svg></div><div><h3>SED UT PERSPICIATIS UNDE OMNIS</h3><p>Nemo enim ipsam voluptatem quia</p></div></div>
  <div class="event" style="border-bottom:none"><div class="event-icon"><svg width="14" height="12"><path d="M2 10V7a5 5 0 0 1 10 0v3" fill="none" stroke="#fff" stroke-width="2"/><rect x="1" y="7" width="3" height="4" fill="#fff"/><rect x="10" y="7" width="3" height="4" fill="#fff"/></svg></div><div><h3>SED UT PERSPICIATIS UNDE OMNIS</h3><p>Nemo enim ipsam voluptatem quia</p></div></div>
</div>

<div class="abs popular-bar">
  <h2>MOST POPULAR</h2>
  <svg width="26" height="16" viewBox="0 0 26 16"><path d="M7 2 1 8 7 14M19 2 25 8 19 14" fill="none" stroke="#fff" stroke-width="1.6"/></svg>
</div>

<article class="abs card" style="left:67px">
  <div style="height:174px;background:linear-gradient(135deg,#3a6fd0,#c9a45c 45%,#7a2a6a 75%,#1a1030)" role="img" aria-label="Photo of young women laughing and dancing at a club party with champagne"></div>
  <svg class="abs" style="left:77px;top:49px" width="56" height="56" viewBox="0 0 56 56"><circle class="play" cx="28" cy="28" r="26"/><path d="M23 18 38 28 23 38Z" fill="rgba(255,255,255,.45)"/></svg>
  <p>Lorem ipsum dolor sit amet, consectetur adipiscing elit. Curabitur</p>
  <div class="meta">Posted by <b>Admin</b> &nbsp;| &nbsp;7 days ago</div>
</article>
<article class="abs card" style="left:299px">
  <div style="height:174px;background:linear-gradient(135deg,#3a3fd0,#b98ad8 45%,#6a2aa0 75%,#201035)" role="img" aria-label="Photo of a DJ in glasses mixing on turntables under purple lights"></div>
  <svg class="abs" style="left:77px;top:49px" width="56" height="56" viewBox="0 0 56 56"><circle class="play" cx="28" cy="28" r="26"/><path d="M23 18 38 28 23 38Z" fill="rgba(255,255,255,.45)"/></svg>
  <p>Lorem ipsum dolor sit amet, consectetur adipiscing elit. Curabitur</p>
  <div class="meta">Posted by <b>Admin</b> &nbsp;| &nbsp;7 days ago</div>
</article>

<aside class="abs albums">
  <h2>RECENTLY ADDED &nbsp;ALBUM</h2>
  <div class="album">
    <div class="thumb" style="background:linear-gradient(135deg,#1a2a6a,#7a90c0,#101830)" role="img" aria-label="Album cover of a singer performing on a blue-lit stage"></div>
    <div><h3>SED UT PERSPICIATIS</h3><p>Lorem ipsum dolor sit amet,<br>consectetur adipiscing elit.</p>
      <div class="stars"><svg width="36" height="7" viewBox="0 0 36 7"><g><path d="M3.5 0 4.5 2.5 7 2.7 5 4.3 5.7 7 3.5 5.5 1.3 7 2 4.3 0 2.7 2.5 2.5Z" fill="#e2a013"/><path transform="translate(9 0)" d="M3.5 0 4.5 2.5 7 2.7 5 4.3 5.7 7 3.5 5.5 1.3 7 2 4.3 0 2.7 2.5 2.5Z" fill="none" stroke="#777" stroke-width=".7"/><path transform="translate(18 0)" d="M3.5 0 4.5 2.5 7 2.7 5 4.3 5.7 7 3.5 5.5 1.3 7 2 4.3 0 2.7 2.5 2.5Z" fill="none" stroke="#777" stroke-width=".7"/><path transform="translate(27 0)" d="M3.5 0 4.5 2.5 7 2.7 5 4.3 5.7 7 3.5 5.5 1.3 7 2 4.3 0 2.7 2.5 2.5Z" fill="none" stroke="#777" stroke-width=".7"/></g></svg></div></div>
  </div>
  <div class="album">
    <div class="thumb" style="background:linear-gradient(180deg,#3a6ae0,#a8c0f0 40%,#151a30)" role="img" aria-label="Album cover of a crowd with raised hands at a concert"></div>
    <div><h3>SED UT PERSPICIATIS</h3><p>Lorem ipsum dolor sit amet,<br>consectetur adipiscing elit.</p>
      <div class="stars"><svg width="36" height="7" viewBox="0 0 36 7"><g><path d="M3.5 0 4.5 2.5 7 2.7 5 4.3 5.7 7 3.5 5.5 1.3 7 2 4.3 0 2.7 2.5 2.5Z" fill="#e2a013"/><path transform="translate(9 0)" d="M3.5 0 4.5 2.5 7 2.7 5 4.3 5.7 7 3.5 5.5 1.3 7 2 4.3 0 2.7 2.5 2.5Z" fill="none" stroke="#777" stroke-width=".7"/><path transform="translate(18 0)" d="M3.5 0 4.5 2.5 7 2.7 5 4.3 5.7 7 3.5 5.5 1.3 7 2 4.3 0 2.7 2.5 2.5Z" fill="none" stroke="#777" stroke-width=".7"/><path transform="translate(27 0)" d="M3.5 0 4.5 2.5 7 2.7 5 4.3 5.7 7 3.5 5.5 1.3 7 2 4.3 0 2.7 2.5 2.5Z" fill="none" stroke="#777" stroke-width=".7"/></g></svg></div></div>
  </div>
  <div class="album">
    <div class="thumb" style="background:linear-gradient(135deg,#4a90e0,#e8c090 45%,#c04050)" role="img" aria-label="Album cover of friends cheering at a summer festival"></div>
    <div><h3>SED UT PERSPICIATIS</h3><p>Lorem ipsum dolor sit amet,<br>consectetur adipiscing elit.</p>
      <div class="stars"><svg width="36" height="7" viewBox="0 0 36 7"><g><path d="M3.5 0 4.5 2.5 7 2.7 5 4.3 5.7 7 3.5 5.5 1.3 7 2 4.3 0 2.7 2.5 2.5Z" fill="#e2a013"/><path transform="translate(9 0)" d="M3.5 0 4.5 2.5 7 2.7 5 4.3 5.7 7 3.5 5.5 1.3 7 2 4.3 0 2.7 2.5 2.5Z" fill="none" stroke="#777" stroke-width=".7"/><path transform="translate(18 0)" d="M3.5 0 4.5 2.5 7 2.7 5 4.3 5.7 7 3.5 5.5 1.3 7 2 4.3 0 2.7 2.5 2.5Z" fill="none" stroke="#777" stroke-width=".7"/><path transform="translate(27 0)" d="M3.5 0 4.5 2.5 7 2.7 5 4.3 5.7 7 3.5 5.5 1.3 7 2 4.3 0 2.7 2.5 2.5Z" fill="none" stroke="#777" stroke-width=".7"/></g></svg></div></div>
  </div>
</aside>

<footer class="abs site-footer">
  <div class="abs social" aria-label="Social network links"><span></span><span></span><span></span><span></span><span></span><span></span></div>
  <p class="abs copyright">Copyright 2015 · All rights reserved.</p>
</footer>

</body>
</html>
```